Logo and Business Card Design

Harbor Crest Logistics provides our customers with one call solutions to packing, trucking and warehousing needs throughout the supply chain.
We need ideas for a logo/business card. I have 2 general concepts.
1. Modern logo involving: the globe, Harbor Crest, arrow, movement, the two words having 2 different fonts/colors, the number 1.
2. Logo involving Lion/Winged Lion: incorporate lion onto globe, tagline "The Pride of the Pack", movement, flowing.

Target Market(s)

International Logistics companies, Air cargo companies, manufacturing companies

Industry/Entity Type

Business

Contact Information for Business Card

Dale Verhoeven
Owner
Harbor Crest Logistics
2874 Wexley Blvd.
Cedar Ford Village, IL 60219
555-308-2946
daleh@harborcrestfreight.example

Font styles to use
Sans Serif

Requirements
Must have
• 1. Modern logo involving: the globe, Harbor Crest, arrow, movement, the two words having 2 different fonts/colors, the number 1.
Nice to have
Should not have
• Do not have too complex of a design.

```html
<!DOCTYPE html>
<html lang="en">
<head>
<meta charset="utf-8">
<title>Harbor Crest Logistics – Business Cards</title>
<link href="https://fonts.googleapis.com/css2?family=Exo+2:wght@400&display=swap" rel="stylesheet">
<style>
  :root {
    --backdrop: #4b4b4d;
    --card-paper: #ffffff;
    --brand-blue: #00aeef;
    --brand-charcoal: #231f20;
    --tab-white: #ffffff;
  }
  html, body {
    margin: 0;
    padding: 0;
    width: 1200px;
    height: 1000px;
    overflow: hidden;
    background: var(--backdrop);
  }
  .canvas {
    position: relative;
    width: 1200px;
    height: 1000px;
  }
  .business-card {
    position: absolute;
    left: 255px;
    width: 700px;
    height: 410px;
  }
  .business-card--blue { top: 83px; --accent: var(--brand-blue); --tab-text: var(--brand-blue); }
  .business-card--dark { top: 527px; --accent: var(--brand-charcoal); --tab-text: var(--brand-charcoal); }
  .business-card svg { display: block; }
  .card-paper { fill: var(--card-paper); }
  .card-panel { fill: var(--accent); }
  .brand-mark { fill: var(--tab-white); }
  .info-tab { fill: var(--tab-white); }
  .card-text {
    font-family: "Exo 2", sans-serif;
    font-weight: 400;
  }
  .company-name { fill: var(--tab-white); font-size: 28px; letter-spacing: 0.6px; }
  .company-address { fill: var(--tab-white); font-size: 20px; letter-spacing: 0.7px; }
  .tab-text { fill: var(--tab-text); font-size: 21px; letter-spacing: 0.3px; }
</style>
</head>
<body>
<main class="canvas">

  <section class="business-card business-card--blue" aria-label="Business card, blue version">
    <svg width="700" height="410" viewBox="0 0 700 410">
      <rect class="card-paper" x="0" y="0" width="700" height="410"/>
      <rect class="card-panel" x="23" y="22" width="654" height="365" rx="8"/>
      <circle class="brand-mark" cx="342" cy="122" r="50"/>
      <text class="card-text company-name" x="342" y="237" text-anchor="middle">Harbor Crest Logistics</text>
      <text class="card-text company-address" x="342" y="261" text-anchor="middle">2874 Wexley Blvd. Cedar Ford Village, IL</text>
      <polygon class="info-tab" points="23,290 305,290 323,306 305,322 23,322"/>
      <text class="card-text tab-text" x="51" y="315">Dale Verhoeven</text>
      <polygon class="info-tab" points="23,330 150,330 167,346 150,362 23,362"/>
      <text class="card-text tab-text" x="51" y="354">Owner</text>
      <polygon class="info-tab" points="677,311 390,311 372,327 390,343 677,343"/>
      <text class="card-text tab-text" x="646" y="335" text-anchor="end">60219 555-308-2946</text>
      <polygon class="info-tab" points="677,350 315,350 296,366 315,382 677,382"/>
      <text class="card-text tab-text" x="646" y="374" text-anchor="end">daleh@harborcrestfreight.example</text>
    </svg>
  </section>

  <section class="business-card business-card--dark" aria-label="Business card, dark version">
    <svg width="700" height="410" viewBox="0 0 700 410">
      <rect class="card-paper" x="0" y="0" width="700" height="410"/>
      <rect class="card-panel" x="23" y="22" width="654" height="365" rx="8"/>
      <circle class="brand-mark" cx="342" cy="122" r="50"/>
      <text class="card-text company-name" x="342" y="237" text-anchor="middle">Harbor Crest Logistics</text>
      <text class="card-text company-address" x="342" y="261" text-anchor="middle">2874 Wexley Blvd. Cedar Ford Village, IL</text>
      <polygon class="info-tab" points="23,290 305,290 323,306 305,322 23,322"/>
      <text class="card-text tab-text" x="51" y="315">Dale Verhoeven</text>
      <polygon class="info-tab" points="23,330 150,330 167,346 150,362 23,362"/>
      <text class="card-text tab-text" x="51" y="354">Owner</text>
      <polygon class="info-tab" points="677,311 390,311 372,327 390,343 677,343"/>
      <text class="card-text tab-text" x="646" y="335" text-anchor="end">60219 555-308-2946</text>
      <polygon class="info-tab" points="677,350 315,350 296,366 315,382 677,382"/>
      <text class="card-text tab-text" x="646" y="374" text-anchor="end">daleh@harborcrestfreight.example</text>
    </svg>
  </section>

</main>
</body>
</html>
```